Vela Link and Wire post card design

We need a postcard to hand out to prospective clients detailing what we do with contact details kept to just a mobile phone number.
Vela Link and Wire is a communications networking company specialising in computer cabling, phone cabling, fibre optics, CCTV, particularly for small business. We offer licenced technicians with over 20 years experience in this field. We service greater Brisbane. Designs that incorporate colours from our logo would be great and that is similar to our business card.
Communications

```html
<!DOCTYPE html>
<html lang="en">
<head>
<meta charset="utf-8">
<title>Vela Link PostCard Design</title>
<link href="https://fonts.googleapis.com/css2?family=Dosis:wght@400;500;600&display=swap" rel="stylesheet">
<style>
  :root {
    --band-green: #5a8a22;
    --brand-green: #3dbd4a;
    --brand-green-soft: #5ec95a;
    --card-black: #000000;
    --ink: #111111;
    --white: #ffffff;
    --rule-grey: #6b6b6b;
    --page: #ffffff;
    --hex-blue: #d6ebf2;
    --hex-cream: #f4f3dc;
  }
  * { margin: 0; padding: 0; box-sizing: border-box; }
  html, body { width: 1200px; height: 905px; overflow: hidden; background: var(--page); }
  body { position: relative; font-family: "Dosis", sans-serif; color: var(--ink); }

  .band { position: absolute; left: 0; width: 1200px; height: 6px; background: var(--band-green); }
  .band--top { top: 0; }
  .band--bottom { bottom: 0; }

  .backdrop { position: absolute; inset: 0; }

  .sheet-title { position: absolute; top: 24px; left: 0; width: 1200px; text-align: center; font-size: 17px; font-weight: 500; letter-spacing: 0.3px; }
  .side-label { position: absolute; font-size: 15px; font-weight: 500; transform: translateX(-50%); }
  .side-label--back { left: 249px; top: 61px; }
  .side-label--front { left: 903px; top: 295px; }

  .card { position: absolute; background: var(--card-black); overflow: hidden; }
  .card--back { left: 15px; top: 87px; width: 500px; height: 388px; }
  .card--front { left: 467px; top: 324px; width: 724px; height: 561px;
    background: radial-gradient(ellipse at 20% 95%, #0d1a0f 0%, #000 55%); }

  .brand { position: absolute; display: flex; align-items: center; gap: 10px; color: var(--brand-green); font-weight: 600; white-space: nowrap; }
  .brand__dot { border-radius: 50%; background: var(--brand-green); flex: none; }
  .card--back .brand { left: 30px; top: 40px; font-size: 27px; }
  .card--back .brand__dot { width: 22px; height: 22px; }
  .card--front .brand { left: 40px; top: 62px; font-size: 40px; }
  .card--front .brand__dot { width: 32px; height: 32px; }

  .back-phone { position: absolute; left: 95px; top: 104px; color: var(--white); font-size: 20px; font-weight: 500; }
  .stamp-box { position: absolute; left: 400px; top: 30px; width: 77px; height: 77px; border: 1px solid #9a9a9a; }
  .address-line { position: absolute; left: 240px; width: 210px; height: 1px;
    background: linear-gradient(90deg, transparent, var(--rule-grey) 12%, var(--rule-grey) 88%, transparent); }

  .fibre-art { position: absolute; right: 0; top: 0; width: 360px; height: 310px;
    background: radial-gradient(ellipse at 85% 20%, rgba(61,189,74,0.75) 0%, rgba(30,140,60,0.45) 35%, rgba(0,0,0,0) 72%); }

  .headline { position: absolute; left: 37px; top: 312px; font-size: 33px; font-weight: 400; color: var(--brand-green-soft); white-space: nowrap; }
  .headline__em { color: var(--white); }

  .services { position: absolute; left: 37px; top: 382px; list-style: none; }
  .services__item { display: flex; align-items: center; gap: 13px; height: 39.5px; font-size: 30px; color: var(--brand-green-soft); }
  .services__bullet { width: 20px; height: 20px; border-radius: 50%; background: #b9c93a; flex: none; }

  .contact { position: absolute; right: 40px; top: 420px; text-align: right; color: var(--white); }
  .contact__name { font-size: 31px; font-weight: 400; line-height: 1.1; }
  .contact__phone { font-size: 35px; font-weight: 400; line-height: 1.3; margin-top: 6px; }
</style>
</head>
<body>
  <div class="band band--top"></div>

  <svg class="backdrop" width="1200" height="905" aria-hidden="true">
    <polygon points="205,548 300,548 360,628 300,724 205,724 162,628" fill="var(--hex-blue)" opacity="0.8"/>
    <polygon points="0,788 150,788 190,880 150,905 0,905" fill="var(--hex-blue)" opacity="0.7"/>
    <polygon points="330,775 470,775 470,905 330,905" fill="var(--hex-cream)" opacity="0.7"/>
  </svg>

  <h1 class="sheet-title">Vela Link PostCard Design</h1>
  <p class="side-label side-label--back">Back</p>
  <p class="side-label side-label--front">Front</p>

  <section class="card card--back">
    <div class="brand"><span class="brand__dot"></span>Vela Link and Wire</div>
    <p class="back-phone">0412 555 018</p>
    <div class="stamp-box"></div>
    <div class="address-line" style="top:194px"></div>
    <div class="address-line" style="top:215px"></div>
    <div class="address-line" style="top:237px"></div>
    <div class="address-line" style="top:259px"></div>
  </section>

  <section class="card card--front">
    <div class="fibre-art" role="img" aria-label="Glowing green fibre optic strands fanning out from the top right corner"></div>
    <div class="brand"><span class="brand__dot"></span>Vela Link and Wire</div>
    <p class="headline">Licensed technician with over <span class="headline__em">20 years</span> experience</p>
    <ul class="services">
      <li class="services__item"><span class="services__bullet"></span>Computer Cabling</li>
      <li class="services__item"><span class="services__bullet"></span>Phone Cabling</li>
      <li class="services__item"><span class="services__bullet"></span>Fibre Optics</li>
      <li class="services__item"><span class="services__bullet"></span>CCTV</li>
    </ul>
    <div class="contact">
      <p class="contact__name">Daniel Harper</p>
      <p class="contact__phone">0412 555 018</p>
    </div>
  </section>

  <div class="band band--bottom"></div>
</body>
</html>
```